We want a business card/punch card for our business. We are including examples of our current business card (we like the front of our business card and not looking to remake it). We need only back side to be designed in form of a punch card (we are including a sample of the punch card we made, but are unsatisfied). For each $180 spend (9 punches) our clients have $20 off.

Colors
886aae

```html
<!DOCTYPE html>
<html lang="en">
<head>
<meta charset="utf-8">
<title>Lumen Path – Appreciation Punch Card</title>
<link rel="stylesheet" href="https://fonts.googleapis.com/css2?family=Tinos:wght@400;700&display=swap">
<style>
  :root {
    --backdrop: #2f2f30;
    --card: #ffffff;
    --ink: #222222;
    --purple: #5b2d8e;
    --blue: #5865b0;
    --wave-grey: #cfcfcf;
    --petal: #e2e2e2;
    --petal-deep: #d2d2d2;
    --figure: #5560a8;
    --slot-ring: #886aae;
  }
  * { box-sizing: border-box; margin: 0; padding: 0; }
  html, body { width: 1200px; height: 1200px; overflow: hidden; }
  body {
    background: var(--backdrop);
    font-family: "Tinos", "Times New Roman", serif;
    position: relative;
  }
  .card {
    position: absolute;
    width: 730px;
    height: 417px;
    background: var(--card);
    overflow: hidden;
  }
  .card--message { left: 235px; top: 105px; }
  .card--value { left: 234px; top: 669px; }

  .petals { position: absolute; border-radius: 50%; }
  .petals--top-right {
    right: -60px; top: -80px; width: 300px; height: 330px;
    background: radial-gradient(ellipse at 60% 40%, var(--petal-deep), var(--petal) 55%, rgba(226,226,226,0) 72%);
  }
  .petals--bottom-left {
    left: -80px; bottom: -40px; width: 320px; height: 260px;
    background: radial-gradient(ellipse at 35% 60%, var(--petal-deep), var(--petal) 50%, rgba(226,226,226,0) 72%);
  }

  .brand {
    position: absolute;
    display: flex;
    align-items: center;
    gap: 8px;
    color: var(--purple);
    font-size: 30px;
    font-weight: 400;
    white-space: nowrap;
  }
  .brand__dot { width: 14px; height: 14px; border-radius: 50%; background: var(--purple); }
  .card--message .brand { left: 50%; top: 100px; transform: translateX(-50%); }
  .card--value .brand { right: 28px; top: 60px; font-size: 26px; }

  .message {
    position: absolute;
    left: 0; right: 0; top: 180px;
    text-align: center;
    font-size: 20.5px;
    line-height: 24.5px;
    color: var(--ink);
    white-space: nowrap;
  }
  .message strong { color: var(--purple); }
  .website {
    position: absolute;
    left: 0; right: 0; top: 335px;
    text-align: center;
    font-size: 19.5px;
    color: var(--purple);
  }

  .wave { position: absolute; left: 0; bottom: 0; width: 100%; height: 60px; }

  .figure-area {
    position: absolute;
    left: 0; top: 62px;
    width: 345px; height: 280px;
    border-radius: 45% 45% 20% 20%;
    background: linear-gradient(180deg, var(--petal) 0%, #b9bcd8 45%, var(--figure) 100%);
  }
  .figure-shadow {
    position: absolute;
    left: 35px; top: 334px; width: 305px; height: 12px;
    border-radius: 50%;
    background: #d9d9d9;
  }

  .offer {
    position: absolute;
    left: 402px; top: 125px;
    color: var(--purple);
  }
  .offer__amount {
    font-size: 64px;
    font-weight: 700;
    line-height: 1;
    color: var(--blue);
  }
  .offer__title {
    margin-top: 2px;
    font-size: 35px;
    line-height: 32px;
    text-transform: uppercase;
  }

  .punches {
    position: absolute;
    left: 402px; top: 318px;
    display: flex;
    gap: 7px;
  }
  .punch {
    width: 27px; height: 27px;
    border-radius: 50%;
    border: 2px solid var(--slot-ring);
    background: var(--card);
  }
  .punch--reward { background: var(--slot-ring); }
</style>
</head>
<body>
  <section class="card card--message">
    <div class="petals petals--top-right" role="img" aria-label="Soft grey lotus petal decoration"></div>
    <div class="petals petals--bottom-left" role="img" aria-label="Soft grey lotus petal decoration"></div>
    <div class="brand"><span class="brand__dot"></span>Lumen Path</div>
    <p class="message">This card is a symbol of appreciation from us to you, without your<br>business we would not be able to what we love most When you fill out<br>this card you will receive <strong>$20</strong> toward your next Weekly Event,<br>Workshop or Private Session.</p>
    <p class="website">www.LumenPathStudio.com</p>
    <svg class="wave" viewBox="0 0 730 60" preserveAspectRatio="none">
      <path d="M0 52 C180 28 360 22 520 40 C620 52 690 38 730 12 L730 60 L0 60 Z" fill="var(--wave-grey)"/>
      <path d="M0 58 C180 36 360 30 520 48 C620 58 690 44 730 22 L730 60 L0 60 Z" fill="var(--blue)"/>
    </svg>
  </section>

  <section class="card card--value">
    <div class="figure-area" role="img" aria-label="Illustration of a person seated in meditation before lotus petals"></div>
    <div class="figure-shadow"></div>
    <div class="brand"><span class="brand__dot"></span>Lumen Path</div>
    <div class="offer">
      <div class="offer__amount">$20</div>
      <div class="offer__title">Lumen<br>Appreciation<br>Card</div>
    </div>
    <div class="punches" aria-label="Nine punch slots">
      <span class="punch"></span><span class="punch"></span><span class="punch"></span>
      <span class="punch"></span><span class="punch"></span><span class="punch"></span>
      <span class="punch"></span><span class="punch"></span><span class="punch"></span>
    </div>
    <svg class="wave" viewBox="0 0 730 60" preserveAspectRatio="none">
      <path d="M0 52 C180 28 360 22 520 40 C620 52 690 38 730 12 L730 60 L0 60 Z" fill="var(--wave-grey)"/>
      <path d="M0 58 C180 36 360 30 520 48 C620 58 690 44 730 22 L730 60 L0 60 Z" fill="var(--purple)"/>
    </svg>
  </section>
</body>
</html>
```